Creat new BusinessCard for Brightpath Advisory!

Hello Creativ Designer. I need a new Businesscard for our brand new Company "Brightpath Coaching". We do Consulting for a better Life & Work Situation. to create Fulfillment, Sense, Motivation and healthy Work Places in Company's. So we try to create a better World and help the employee to like what they do!
So we would like to have 2 Sites on the card. On the Back we want to put this words: "The sole meaning of life, is to serve humanity" (it can be vertical oder horizontal). In the front there is the Logo (Black or White) and Adress+ and Slogan.

Slogan on the front: -Make your Business & Life to a better place-

Name: Lukas Fenwald
Titel: Founder - Visionary - Trainer
Adress: Based in Switzerland

Tel: +41 (0) 71 483 27 15
Email: hello@brightpath-coaching.ch
Homepage: www.brightpath-coaching.ch

Thanks for your inspired Ideas and your help to make the world to a better place! IT has to be ready to print and normal Size.

Target Market(s)

insurance, Bank, Telecom, industry, IT, Medical

Contact Information for Business Card

Breite: 85 mm x Höhe: 55 mm

Colors

Designer to choose colors to be used in the design.

Requirements
Nice to have
• Thanks for your Ideas so far!
• Maybe you can try/play with the colors: Purple Code #652C8F and Grey #979797 from the Zorvik Logo purple and grey (but only a soft combination, not to much)

```html
<!DOCTYPE html>
<html lang="en">
<head>
<meta charset="utf-8">
<title>Brightpath Coaching – Business Card</title>
<link rel="stylesheet" href="https://fonts.googleapis.com/css2?family=Didact+Gothic&family=Open+Sans:ital,wght@1,600&display=swap">
<style>
  :root {
    --backdrop: #2a2d31;
    --card: #ffffff;
    --purple: #4b22d6;
    --purple-soft: #6a4fcf;
    --grey: #8a98a3;
    --ink: #2f3e48;
    --rule-grey: #9aa3ab;
  }
  * { margin: 0; padding: 0; box-sizing: border-box; }
  html, body { width: 1200px; height: 1000px; overflow: hidden; }
  body {
    background: var(--backdrop);
    position: relative;
    font-family: "Didact Gothic", sans-serif;
  }
  .card {
    position: absolute;
    background: var(--card);
    overflow: hidden;
    box-shadow: 0 6px 14px rgba(0,0,0,0.45);
  }

  /* Front */
  .card-front { left: 352px; top: 108px; width: 524px; height: 339px; }
  .brand {
    position: absolute; left: 0; right: 0; top: 97px;
    display: flex; flex-direction: column; align-items: center;
  }
  .brand-dot {
    width: 80px; height: 80px; border-radius: 50%;
    background: linear-gradient(135deg, var(--purple), var(--purple-soft));
  }
  .brand-name {
    margin-top: 12px;
    font-size: 25px; letter-spacing: 0.5px;
    color: var(--purple);
  }
  .brand-sub {
    margin-top: 2px; font-size: 11px; letter-spacing: 3px;
    color: var(--purple);
    display: flex; align-items: center; gap: 8px;
  }
  .brand-sub::before, .brand-sub::after {
    content: ""; width: 38px; height: 1px; background: var(--rule-grey);
  }
  .slogan-band {
    position: absolute; left: 0; right: 0; top: 289px;
    display: flex; align-items: center; gap: 6px;
    font-size: 9.5px; color: var(--purple);
  }
  .slogan-band .rule { flex: 1; height: 2px; }
  .slogan-band .rule-left { background: linear-gradient(90deg, var(--rule-grey), var(--purple)); }
  .slogan-band .rule-right { background: linear-gradient(90deg, var(--purple), var(--rule-grey)); }

  /* Back */
  .card-back { left: 350px; top: 543px; width: 530px; height: 341px; }
  .accent-circle {
    position: absolute; left: -7px; top: -4px; width: 243px; height: 243px;
    border-radius: 50%;
    background: linear-gradient(180deg, var(--purple) 0%, #6b5ac4 45%, #8996a4 100%);
  }
  .person { position: absolute; left: 255px; top: 73px; color: var(--ink); }
  .person-name { font-size: 23px; line-height: 28px; }
  .person-role { font-size: 17px; line-height: 22px; }
  .contact-list { position: absolute; left: 255px; top: 152px; list-style: none; color: var(--ink); }
  .contact-list li {
    display: flex; align-items: center; gap: 10px;
    font-size: 17.5px; height: 31px;
  }
  .contact-list svg { width: 17px; height: 17px; fill: var(--ink); }
  .quote {
    position: absolute; left: 20px; top: 262px; width: 494px; height: 70px;
    font-family: "Open Sans", sans-serif; font-style: italic; font-weight: 600;
    color: var(--grey); font-size: 19.5px; line-height: 22px;
  }
  .quote .mark { position: absolute; width: 42px; height: 34px; fill: var(--grey); }
  .quote .mark-open { left: 0; top: 2px; }
  .quote .mark-close { right: 0; top: 32px; }
  .quote .line-1 { position: absolute; left: 52px; top: 12px; white-space: nowrap; }
  .quote .line-2 { position: absolute; left: 222px; top: 34px; white-space: nowrap; }
</style>
</head>
<body>

<section class="card card-front" aria-label="Card front">
  <div class="brand">
    <div class="brand-dot"></div>
    <div class="brand-name">BRIGHTPATH</div>
    <div class="brand-sub">COACHING</div>
  </div>
  <div class="slogan-band">
    <span class="rule rule-left"></span>
    <span class="slogan">"Make your Business &amp; Life to a better place"</span>
    <span class="rule rule-right"></span>
  </div>
</section>

<section class="card card-back" aria-label="Card back">
  <div class="accent-circle"></div>

  <div class="person">
    <div class="person-name">Lukas Fenwald</div>
    <div class="person-role">Founder | Visionary | Trainer</div>
  </div>

  <ul class="contact-list">
    <li>
      <svg viewBox="0 0 24 24"><path d="M6.6 10.8a15.1 15.1 0 0 0 6.6 6.6l2.2-2.2c.3-.3.7-.4 1-.2 1.1.4 2.3.6 3.6.6.6 0 1 .4 1 1V20c0 .6-.4 1-1 1A17 17 0 0 1 3 4c0-.6.4-1 1-1h3.5c.6 0 1 .4 1 1 0 1.3.2 2.5.6 3.6.1.3 0 .7-.2 1z"/></svg>
      +41 (0) 71 483 27 15
    </li>
    <li>
      <svg viewBox="0 0 24 24"><path d="M2 5h20v14H2z" fill="none"/><path d="M2 6l10 7 10-7V5H2zm0 2.4V19h20V8.4l-10 7z"/></svg>
      hello@brightpath-coaching.ch
    </li>
    <li>
      <svg viewBox="0 0 24 24" fill="none" stroke="#2f3e48" stroke-width="1.6"><circle cx="12" cy="12" r="9"/><ellipse cx="12" cy="12" rx="4" ry="9"/><path d="M3 12h18M5 7h14M5 17h14"/></svg>
      www.brightpath-coaching.ch
    </li>
  </ul>

  <blockquote class="quote">
    <svg class="mark mark-open" viewBox="0 0 42 34"><path d="M0 34V18C0 8 5 2 15 0v6c-5 2-7 5-7 10h7v18zm23 0V18c0-10 5-16 15-18v6c-5 2-7 5-7 10h7v18z"/></svg>
    <span class="line-1">The sole meaning of life,</span>
    <span class="line-2">is to serve humanity</span>
    <svg class="mark mark-close" viewBox="0 0 42 34"><path d="M4 0h15v16c0 10-5 16-15 18v-6c5-2 7-5 7-10H4zm23 0h15v16c0 10-5 16-15 18v-6c5-2 7-5 7-10h-7z"/></svg>
  </blockquote>
</section>

</body>
</html>
```